Community-based social network needs a new landing page

We need a landing page for a local social network in Singapore called "NestLinker.sg". It is a website that help neighbours to connect with each other for mutual benefits such as providing professional/non-professional services, sharing items, and neighbourly help, etc.

There is an existing website but we want to completely revamp it. It is most important that the new landing page communicates that the neighbourhood has skills and services for people to discover.

The final design of the landing page should be modern, and communicates a sense of community and vibrancy. As a matter of priority, more real estate should be accorded to the neighbours providing services elements.

We have drafted 2 reference sites that communicates the key ideas/user propositions for your easy reference:
http://tavrilo82.pageforge.example/nestlinker
http://tavrilo82.pageforge.example/nestlinker2

As long as the key ideas/user propositions are kept to, we are open to any design proposals. I.e. you do not have to follow the design layout of the reference sites

Target Market(s)

Our target market is primarily the Singapore community, includes all genders, education levels and occupations, aged between 17-45 years old.

In the file uploaded, you will find pictures of Singapore neighbourhoods and people of local ethnicities. Please use them, but you may arrange and add further filters to better enhance them

Industry/Entity Type

Real Estate

Requirements
Nice to have
• Landing page could be similar to that of www.gatherkite.example, not just at the top, but also the way the other categories are presented at the bottom.

```html
<!DOCTYPE html>
<html lang="en">
<head>
<meta charset="utf-8">
<title>NestLinker.sg – Meet People in Singapore</title>
<link href="https://fonts.googleapis.com/css2?family=Libre+Baskerville&family=Questrial&family=Ubuntu:wght@400;500&display=swap" rel="stylesheet">
<style>
:root{
  --panel:#dce9f5;
  --panel-line:#b9c8d6;
  --teal:#3fa3c0;
  --red:#c8302c;
  --navy:#1c3e6b;
  --green:#6a8f1d;
  --ink:#222;
  --muted:#8a8f95;
  --footer:#222222;
  --white:#fff;
}
*{box-sizing:border-box;margin:0;padding:0}
html,body{width:1200px;height:1129px;overflow:hidden}
body{position:relative;background:#fff;font-family:"Questrial",sans-serif;color:var(--ink)}
.abs{position:absolute}

.hero{left:0;top:0;width:1200px;height:593px;background:linear-gradient(180deg,#7d8791 0%,#9aa3ab 30%,#6d7680 60%,#5c5a55 85%,#6b5e52 100%)}
.hero-title{left:142px;top:212px;font-family:"Libre Baskerville",serif;font-size:58px;line-height:57px;color:var(--white);letter-spacing:1px}
.hero-btn{left:143px;top:407px;width:146px;height:32px;background:var(--red);border-radius:5px;color:#fff;font-family:"Ubuntu",sans-serif;font-weight:500;font-size:16px;text-align:center;line-height:32px}
.bubble{border:2px solid #fff;border-radius:6px;background:linear-gradient(135deg,#c9a58a,#7d6757)}
.pointers{left:0;top:0}

.topbar{left:120px;top:0;width:960px;height:96px;background:var(--panel)}
.brand{left:133px;top:28px;display:flex;align-items:center;gap:8px;font-family:"Questrial",sans-serif;font-size:30px;color:#3a3a3a}
.brand-dot{width:22px;height:22px;background:var(--teal)}
.login-label{font-family:"Libre Baskerville",serif;font-size:12px;color:#222}
.field{background:#fff;border:1px solid #c6d3df;border-radius:2px;height:20px}
.small{font-family:"Libre Baskerville",serif;font-size:10px;color:#222}
.btn-login{left:892px;top:38px;width:60px;height:18px;background:var(--teal);color:#fff;font-size:12px;text-align:center;line-height:18px;border-radius:2px}
.btn-connect{left:996px;top:37px;width:71px;height:21px;background:#4a68a5;border-radius:3px;color:#fff;font-size:11px;line-height:21px;padding-left:6px;display:flex;align-items:center;gap:5px}
.btn-connect span{width:10px;height:10px;background:#fff;display:inline-block}

.content{left:120px;top:570px;width:960px;height:492px;background:var(--panel)}
.feature-icon{width:66px;height:66px;background:var(--teal);border-radius:3px}
.feature-title{font-size:23px;color:#222;letter-spacing:.5px}
.feature-text{font-size:14px;color:#555;line-height:19px;letter-spacing:.5px}
.divider{left:141px;top:695px;width:920px;height:1px;background:var(--panel-line)}
.sec-title{font-family:"Ubuntu",sans-serif;font-size:24px;top:727px}

.links-box{left:130px;top:763px;width:296px;height:245px;background:#fff;border:3px solid #e4ecf3}
.post{position:absolute;left:12px;width:265px}
.post-photo{position:absolute;left:0;top:0;width:54px;height:54px;border-radius:4px;background:linear-gradient(135deg,#b89677,#6d5846)}
.post-title{position:absolute;left:62px;top:0;font-family:"Ubuntu",sans-serif;font-size:13px;color:#111;width:192px;padding-bottom:4px;border-bottom:1px dotted #bbb}
.post-body{position:absolute;left:63px;top:26px;font-family:"Ubuntu",sans-serif;font-size:11.5px;color:#444;line-height:15px;width:192px}
.post-meta{position:absolute;left:63px;top:70px;font-size:11px;color:#9aa;width:205px;display:flex;justify-content:space-between}
.scroll{left:411px;top:775px;width:6px;height:215px;background:#e8eef4;border-radius:3px}

.member{width:66px;height:66px;border:2px solid #fff}
.tagline{left:451px;top:940px;font-family:"Ubuntu",sans-serif;font-size:19px;color:#9aa0a6;line-height:24px;width:310px}
.show-all{left:452px;top:996px;font-size:11px;text-decoration:underline;color:#333}

.join-box{left:771px;top:762px;width:300px;height:252px;background:#eef4fa;border:3px solid #bdd3ea}
.signup{left:796px;top:776px;font-size:16px;letter-spacing:1px;color:#222}
.signup-line{left:786px;top:805px;width:273px;height:1px;background:#9aa}
.input{left:795px;width:249px;height:28px;background:#fff;border:1px solid #c8cfd6;font-size:14px;letter-spacing:1px;color:#555;padding-left:18px;line-height:26px}
.btn-next{left:795px;top:904px;width:77px;height:30px;background:linear-gradient(#eee,#d4d4d4);border:1px solid #aaa;font-size:15px;color:#555;text-align:center;line-height:28px;letter-spacing:1px}
.agree{left:934px;top:909px;font-size:11px;color:#333;display:flex;gap:8px;align-items:center}
.agree span{width:12px;height:12px;border:1px solid #3a6aa0;background:#fff;display:inline-block}
.tiny-link{left:795px;font-size:9.5px;color:#555;letter-spacing:.8px}

.footer{left:0;top:1062px;width:1200px;height:67px;background:var(--footer);color:#fff;font-family:"Ubuntu",sans-serif;font-size:13px}
.share{height:16px;font-size:9px;text-align:center;line-height:16px;border-radius:2px}
</style>
</head>
<body>

<div class="abs hero" role="img" aria-label="Photograph of the Singapore city skyline with high-rise towers"></div>
<h1 class="abs hero-title">MEET<br>PEOPLE IN<br>SINGAPORE</h1>
<div class="abs hero-btn">Try it Yourself</div>

<svg class="abs pointers" width="1200" height="593" aria-hidden="true">
  <path d="M730 287 L765 338 L742 287Z" fill="#fff"/>
  <path d="M955 285 L912 294 L962 290Z" fill="#fff"/>
  <path d="M722 408 L758 388 L722 414Z" fill="#fff"/>
  <path d="M955 386 L934 338 L964 386Z" fill="#fff"/>
</svg>
<div class="abs bubble" style="left:679px;top:209px;width:78px;height:79px" role="img" aria-label="Portrait photo of a community member"></div>
<div class="abs bubble" style="left:953px;top:221px;width:68px;height:70px" role="img" aria-label="Portrait photo of a community member"></div>
<div class="abs bubble" style="left:666px;top:390px;width:58px;height:58px" role="img" aria-label="Portrait photo of a community member"></div>
<div class="abs bubble" style="left:940px;top:384px;width:72px;height:72px" role="img" aria-label="Portrait photo of a community member"></div>

<header class="abs topbar"></header>
<div class="abs brand"><span class="brand-dot"></span>NestLinker.sg</div>
<label class="abs login-label" style="left:509px;top:18px">Username or Email</label>
<div class="abs field" style="left:507px;top:37px;width:182px"></div>
<div class="abs small" style="left:511px;top:59px;display:flex;gap:8px;align-items:center"><span style="width:8px;height:8px;background:#4a5a6a;display:inline-block"></span>Remember me logged in</div>
<label class="abs login-label" style="left:701px;top:18px">Password</label>
<div class="abs field" style="left:698px;top:37px;width:182px"></div>
<div class="abs small" style="left:701px;top:59px">Forgotten your password?</div>
<div class="abs btn-login">Login</div>
<div class="abs small" style="left:967px;top:41px;font-size:11px">OR</div>
<div class="abs btn-connect"><span></span>Connect</div>

<main class="abs content"></main>

<div class="abs feature-icon" style="left:151px;top:595px">
  <svg width="66" height="66" aria-hidden="true"><circle cx="33" cy="26" r="6" fill="#fff"/><path d="M21 43 Q21 34 33 34 Q45 34 45 43Z" fill="#fff"/></svg>
</div>
<div class="abs feature-title" style="left:234px;top:597px">Professional</div>
<div class="abs feature-text" style="left:235px;top:627px">Lorem Ipsum Dolor Sit<br>amet type</div>

<div class="abs feature-icon" style="left:451px;top:595px">
  <svg width="66" height="66" aria-hidden="true"><path d="M22 24 H34 M22 24 V45 H43 V33" stroke="#fff" stroke-width="3" fill="none"/><path d="M30 38 L31 32 L42 21 L47 26 L36 37Z" fill="#fff"/></svg>
</div>
<div class="abs feature-title" style="left:534px;top:597px">Non-Professional</div>
<div class="abs feature-text" style="left:535px;top:627px">Lorem Ipsum Dolor Sit amet<br>type</div>

<div class="abs feature-icon" style="left:785px;top:595px">
  <svg width="66" height="66" aria-hidden="true"><path d="M20 33 L29 43 L47 22" stroke="#fff" stroke-width="5" fill="none"/></svg>
</div>
<div class="abs feature-title" style="left:868px;top:597px;line-height:28px">Selling, helping<br>borrowing,landing</div>

<div class="abs divider"></div>

<h2 class="abs sec-title" style="left:130px;color:var(--navy)">QUICK LINKS</h2>
<h2 class="abs sec-title" style="left:450px;color:var(--red)">LATEST MEMBERS</h2>
<h2 class="abs sec-title" style="left:770px;color:var(--green)">JOIN US</h2>

<section class="abs links-box">
  <article class="post" style="top:27px">
    <div class="post-photo" role="img" aria-label="Member portrait photo"></div>
    <div class="post-title">Composition et la mise en.</div>
    <p class="post-body">Lorem Ipsum est simplement du faux texte employé dans la sition et la misen page avant...</p>
    <div class="post-meta"><span>5 comment <b style="color:#7ab82c">+</b></span><span>▲ ▼</span><span>4 July 2012</span></div>
  </article>
  <article class="post" style="top:131px">
    <div class="post-photo" role="img" aria-label="Member portrait photo" style="background:linear-gradient(135deg,#e0c090,#a07a5a)"></div>
    <div class="post-title">Composition et la mise en.</div>
    <p class="post-body">Lorem Ipsum est simplement du faux texte employé dans la sition et la misen page avant...</p>
    <div class="post-meta"><span>5 comment <b style="color:#7ab82c">+</b></span><span>▲ ▼</span><span>4 July 2012</span></div>
  </article>
</section>
<div class="abs scroll"></div>
<svg class="abs" style="left:406px;top:774px" width="18" height="226" aria-hidden="true">
  <circle cx="9" cy="9" r="8" fill="#4d8fd6"/><path d="M5 11 L9 7 L13 11" stroke="#fff" stroke-width="2" fill="none"/>
  <rect x="6" y="30" width="5" height="40" rx="2" fill="#7aa7d6"/>
  <circle cx="9" cy="215" r="8" fill="#4d8fd6"/><path d="M5 213 L9 217 L13 213" stroke="#fff" stroke-width="2" fill="none"/>
</svg>

<div class="abs member" style="left:451px;top:763px;background:#5a5648" role="img" aria-label="Member photo"></div>
<div class="abs member" style="left:526px;top:763px;background:#cbb8a6" role="img" aria-label="Member photo"></div>
<div class="abs member" style="left:601px;top:763px;background:#8a5a48" role="img" aria-label="Member photo"></div>
<div class="abs member" style="left:676px;top:763px;background:#d8d6d2" role="img" aria-label="Member photo"></div>
<div class="abs member" style="left:451px;top:838px;background:#d9d2c8" role="img" aria-label="Member photo"></div>
<div class="abs member" style="left:526px;top:838px;background:#d2774a" role="img" aria-label="Member photo"></div>
<div class="abs member" style="left:601px;top:838px;background:#3a3432" role="img" aria-label="Member photo"></div>
<div class="abs member" style="left:676px;top:838px;background:#6a6c70" role="img" aria-label="Member photo"></div>
<p class="abs tagline">LOREM IPSUM DOLOR SIT AMET,<br>CONS ECTETUR ADIPISCING ELIT</p>
<a class="abs show-all">SHOW ALL</a>

<section class="abs join-box"></section>
<div class="abs signup">SIGN UP</div>
<div class="abs signup-line"></div>
<div class="abs input" style="top:826px">Username</div>
<div class="abs input" style="top:865px">Password</div>
<div class="abs btn-next">Next</div>
<div class="abs agree">I Agree <span></span></div>
<div class="abs tiny-link" style="top:966px">FORGOT PASSWORD ?</div>
<div class="abs tiny-link" style="top:986px">RESEND ACTIVATION CODE</div>

<footer class="abs footer">
  <span class="abs" style="left:124px;top:24px">copyright©2013. All Rights Reserved</span>
  <span class="abs" style="left:758px;top:24px">Spread the nestlinker</span>
  <div class="abs share" style="left:926px;top:1086px;position:fixed;width:41px;background:#eceef3;color:#3b5998">Like</div>
  <div class="abs share" style="left:978px;top:1086px;position:fixed;width:35px;background:#2f6fcf;color:#fff">+1</div>
  <div class="abs share" style="left:1020px;top:1086px;position:fixed;width:45px;background:#e4f1f9;color:#2a7ab8">Tweet</div>
</footer>

</body>
</html>
```